Selbsthilfegruppe für organtransplantierte Personen sucht Flyer-Design
Sehr schnelle Reaktion auf Änderungswünsche und top Support bis zum Druck :) Gerne wieder!
Zielgruppe
Wir sind eine Selbsthilfegruppe für organtransplantierte Personen, Zielgruppe sind Personen aus der Region die auch ein Spenderorgan empfangen haben und deren Angehörige, die Beistand und Information suchen sowie gemeinsame Aktivitäten wahrnehmen möchten.
Aufgabenstellung
Es gibt bereits einen Flyer der jedoch überarbeitet und etwas schöner und moderner gestaltet werden soll. Der Text kann bestehen bleiben und die Aufteilung muss nicht zwingend geändert werden, anstelle der aktuellen Fotos sollen dann andere eingefügt werden, die übergeben werden, sobald das Design akzeptiert wurde. Es geht hauptsächlich um das Design selbst, es soll ansprechen, freundlich, modern und hoffnungsvoll sein, die Grundfarbe sollte grün sein. Das Logo kann beibehalten aber farblich auch gerne angepasst werden. Es soll ein normaler Faltflyer sein, 2 Faltungen und damit vorn und hinten je 3 einzelne Bereiche wie aktuell, Gesamtmaß A4. Bei Rückfragen gerne melden!

```html
<!DOCTYPE html>
<html lang="de">
<head>
<meta charset="utf-8">
<title>Faltflyer – Innenseite</title>
<link href="https://fonts.googleapis.com/css2?family=Pinyon+Script&family=Quicksand:wght@500&display=swap" rel="stylesheet">
<style>
  :root{
    --green:#6aa33a;
    --green-text:#5b9330;
    --paper:#ffffff;
    --backdrop:#d4d5d8;
    --photo-warm:#c7734c;
    --photo-deep:#6d3a2c;
    --suit:#3a3f55;
  }
  *{margin:0;padding:0;box-sizing:border-box}
  html,body{width:1200px;height:675px;overflow:hidden;background:var(--backdrop)}
  .flyer{
    position:absolute;left:137px;top:10px;width:926px;height:654px;
    background:var(--paper);overflow:hidden;
    box-shadow:0 6px 14px rgba(0,0,0,.25);
    font-family:'Quicksand',sans-serif;font-weight:500;color:var(--green-text);
  }
  .flyer-shapes{position:absolute;inset:0}
  .heading{
    position:absolute;font-family:'Pinyon Script',cursive;font-weight:400;
    color:var(--green-text);font-size:40px;line-height:1;
    border-bottom:1px solid var(--green-text);padding:0 2px 0;
  }
  .heading--about{left:154px;top:66px}
  .heading--together{left:386px;top:36px;font-size:38px}
  .about-text{position:absolute;left:31px;width:300px;font-size:15.5px;line-height:20px}
  .about-text p{margin:0}
  .block-1{top:126px}
  .block-2{top:205px}
  .block-3{top:324px}
  .block-4{top:423px}
  .caption{position:absolute;font-size:15.5px;line-height:20px}
  .caption--inform{left:490px;top:230px}
  .caption--discuss{left:342px;top:418px}
  .caption--celebrate{left:490px;top:612px;color:var(--paper)}
  .outreach{
    position:absolute;left:638px;top:522px;width:275px;
    font-size:15.5px;line-height:20px;color:var(--paper);
  }
</style>
</head>
<body>
<div class="flyer">
  <svg class="flyer-shapes" viewBox="0 0 926 654" width="926" height="654">
    <defs>
      <linearGradient id="speakerPhoto" x1="0" y1="0" x2="1" y2="1">
        <stop offset="0" stop-color="var(--photo-warm)"/>
        <stop offset=".45" stop-color="var(--photo-deep)"/>
        <stop offset="1" stop-color="var(--suit)"/>
      </linearGradient>
      <linearGradient id="photoFade" x1="0" y1="0" x2="0" y2="1">
        <stop offset=".55" stop-color="#fff" stop-opacity="0"/>
        <stop offset="1" stop-color="#fff" stop-opacity="1"/>
      </linearGradient>
      <linearGradient id="audiencePhoto" x1="0" y1="0" x2="0" y2="1">
        <stop offset="0" stop-color="#e9e6e2"/>
        <stop offset="1" stop-color="#6a5448"/>
      </linearGradient>
      <linearGradient id="circlePhoto" x1="0" y1="0" x2="1" y2="1">
        <stop offset="0" stop-color="#b48a6a"/>
        <stop offset="1" stop-color="#6f6a66"/>
      </linearGradient>
      <radialGradient id="partyPhoto" cx=".5" cy=".35" r=".7">
        <stop offset="0" stop-color="#9fc3e8"/>
        <stop offset="1" stop-color="#1c2a4a"/>
      </radialGradient>
    </defs>

    <path d="M0,0 H432 C260,22 90,72 0,121 Z" fill="var(--green)"/>

    <g role="img" aria-label="Foto: Redner vor unscharfem Publikum in einem Vortragssaal">
      <rect x="618" y="0" width="308" height="500" fill="url(#speakerPhoto)"/>
      <rect x="618" y="0" width="308" height="500" fill="url(#photoFade)"/>
    </g>

    <path d="M0,598 C320,562 700,520 926,415 V654 H0 Z" fill="var(--paper)"/>
    <path d="M0,601 C320,565 700,523 926,421 V654 H0 Z" fill="var(--green)"/>

    <circle cx="417.5" cy="168" r="81" fill="url(#audiencePhoto)" stroke="var(--green)" stroke-width="2" role="img" aria-label="Foto: Publikum bei einem Fachvortrag"/>
    <line x1="425" y1="249" x2="586" y2="249" stroke="var(--green)" stroke-width="2"/>

    <circle cx="504" cy="356" r="81" fill="url(#circlePhoto)" stroke="var(--green)" stroke-width="2" role="img" aria-label="Foto: Gesprächskreis mit Stühlen im Kreis"/>
    <line x1="327" y1="437" x2="495" y2="437" stroke="var(--green)" stroke-width="2"/>

    <circle cx="419" cy="543" r="82" fill="url(#partyPhoto)" stroke="var(--paper)" stroke-width="2" role="img" aria-label="Foto: feiernde Menschen im Konfettiregen"/>
  </svg>

  <h2 class="heading heading--about">Über uns</h2>
  <h2 class="heading heading--together">Gemeinsam</h2>

  <div class="about-text block-1"><p>Wir sind …<br>eine Gruppe von Betroffenen und de-<br>ren Angehörige.</p></div>
  <div class="about-text block-2"><p>Wir möchten …<br>Erfahrungen austauschen,<br>Fachvorträge besuchen, aber nicht<br>nur über Krankheit reden, sondern<br>auch miteinander fröhlich sein.</p></div>
  <div class="about-text block-3"><p>Wir organisieren gemeinsam …<br>regelmäßige Treffen, Fachvorträge,<br>Infoveranstaltungen, gesellige<br>Zusammenkünfte und einiges mehr.</p></div>
  <div class="about-text block-4"><p>Wir treffen uns …<br>regelmäßig am letzten Dienstag<br>des Monats um 15:00 Uhr im<br>Familienzentrum ‚Mathilde‘,<br>Lindenweg 12 in Bad<br>Wiesenau.</p></div>

  <span class="caption caption--inform">… informieren</span>
  <span class="caption caption--discuss">… diskutieren</span>
  <span class="caption caption--celebrate">… feiern</span>

  <p class="outreach">… wollen wir mit öffentlichen Aktio-<br>nen viele Menschen erreichen und<br>über unsere Arbeit informieren.</p>
</div>
</body>
</html>
```